Church Christmas Flyer

The flyer is to advertise our Christmas Eve services. The flyer is for a Christian church service to celebrate the birth of Jesus. We would like to see designs that use blue, silver and gold for colors but feel free to be creative. We are interested in a flyer that is has texture, depth and is more abstract than literal. Don't be afraid to layer. Please make the flyer double sided

* I uploaded our Christmas flyer from last year.

Target Market(s)

30-55 year old, male and female

Industry/Entity Type

Church

Requirements
Must have
• Map to the church
Church phone number 555-317-4096
Service times 3:00pm and 5:00pm
church address 28315 Marigold Ave, Hesperia, Ca. 92345
church website www.brookfieldfellowshipnt.com
Scripture verse

Text must stand out and be easy to read
Nice to have
• Use of the star in the sky that guided the wise men to Jesus.
Should not have
• Santa Clause, Snowmen, Reindeer

```html
<!DOCTYPE html>
<html lang="en">
<head>
<meta charset="utf-8">
<title>Christmas Eve Flyer – Brookfield Fellowship</title>
<link rel="stylesheet" href="https://fonts.googleapis.com/css2?family=Arimo:ital,wght@0,400;1,400&display=swap">
<style>
  :root {
    --page: #ffffff;
    --sky-light: #cfe8ef;
    --sky-mid: #4f9dbd;
    --sky-deep: #2f7ea6;
    --crimson: #c40017;
    --crimson-deep: #a80012;
    --silver: #d9dde0;
    --gold: #c9a227;
    --white: #ffffff;
    --snow: #f4efe6;
    --hill: #e8c9a6;
    --tree-blue: #2c6fd0;
    --bell-gold: #d8b640;
    --holly: #2f7a2a;
    --map-paper: #ece8d8;
    --ring-red: #d8323f;
  }
  * { box-sizing: border-box; margin: 0; padding: 0; }
  html, body { width: 1200px; height: 900px; overflow: hidden; background: var(--page); }
  body { position: relative; font-family: "Arimo", Arial, sans-serif; color: var(--white); }

  .flyer-side { position: absolute; left: 171px; width: 816px; height: 361px; overflow: hidden; }
  .flyer-side--front { top: 71px; }
  .flyer-side--back { top: 469px; }
  .side-art { position: absolute; inset: 0; width: 100%; height: 100%; }

  .church-name {
    position: absolute; left: 16px; bottom: 10px;
    font-size: 26px; font-weight: 400; color: var(--white); letter-spacing: 0.5px;
  }

  .scripture {
    position: absolute; left: 20px; top: 16px; width: 530px;
    font-style: italic; font-size: 15px; line-height: 18px; text-transform: uppercase;
  }
  .scripture-ref { display: block; text-align: right; text-transform: none; font-size: 16px; margin-right: 20px; }

  .event-title {
    position: absolute; right: 10px; top: 266px; text-align: right;
  }
  .event-title h1 { font-weight: 400; font-size: 35px; line-height: 38px; letter-spacing: 0.5px; }
  .event-title p { font-style: italic; font-size: 20px; line-height: 26px; }

  .service-details {
    position: absolute; right: 10px; top: 236px; text-align: right;
    font-style: italic; font-size: 18px; line-height: 24px; list-style: none;
  }
</style>
</head>
<body>

<section class="flyer-side flyer-side--front" aria-label="Flyer front">
  <svg class="side-art" viewBox="0 0 816 361" preserveAspectRatio="none">
    <defs>
      <radialGradient id="sky-front" cx="0.9" cy="0.45" r="0.9">
        <stop offset="0" stop-color="var(--sky-light)"/>
        <stop offset="0.35" stop-color="var(--sky-mid)"/>
        <stop offset="1" stop-color="var(--sky-deep)"/>
      </radialGradient>
      <linearGradient id="hill-front" x1="0" y1="0" x2="0" y2="1">
        <stop offset="0" stop-color="var(--snow)"/>
        <stop offset="1" stop-color="var(--hill)"/>
      </linearGradient>
    </defs>
    <rect width="816" height="361" fill="url(#sky-front)"/>
    <g fill="var(--white)">
      <path d="M590 20 l3 14 l14 3 l-14 3 l-3 14 l-3 -14 l-14 -3 l14 -3z"/>
      <path d="M785 70 l2 8 l8 2 l-8 2 l-2 8 l-2 -8 l-8 -2 l8 -2z"/>
      <circle cx="220" cy="120" r="1.5"/><circle cx="320" cy="150" r="1.2"/>
      <circle cx="470" cy="140" r="1.5"/><circle cx="660" cy="60" r="1.2"/>
      <circle cx="720" cy="30" r="1.5"/><circle cx="400" cy="200" r="1.2"/>
    </g>
    <rect role="img" aria-label="Illustration: snowy hill with a small cottage and frosted trees" x="0" y="140" width="190" height="130" rx="60" fill="url(#hill-front)"/>
    <rect role="img" aria-label="Illustration: blue snow-covered pine trees" x="683" y="116" width="133" height="104" rx="30" fill="var(--tree-blue)" opacity="0.85"/>
    <path d="M0 262 C120 270 200 290 300 278 C480 256 640 226 816 222 L816 361 L0 361Z" fill="var(--crimson)"/>
    <path d="M0 250 C120 258 200 278 300 266 C480 244 640 214 816 210" fill="none" stroke="var(--silver)" stroke-width="10"/>
    <path d="M0 260 C120 268 200 288 300 276 C480 254 640 224 816 220" fill="none" stroke="var(--gold)" stroke-width="4"/>
    <rect role="img" aria-label="Illustration: golden Christmas bells with a bow" x="529" y="189" width="133" height="87" rx="40" fill="var(--bell-gold)"/>
  </svg>
  <blockquote class="scripture">
    "This is how God showed his love among us! He sent his one and only Son into the world that we might live through him."
    <cite class="scripture-ref">John 4:9</cite>
  </blockquote>
  <div class="event-title">
    <h1>CHRISTMAS EVE</h1>
    <p>A celebration of God's Love</p>
  </div>
  <p class="church-name">Brookfield Fellowship</p>
</section>

<section class="flyer-side flyer-side--back" aria-label="Flyer back">
  <svg class="side-art" viewBox="0 0 816 361" preserveAspectRatio="none">
    <defs>
      <radialGradient id="sky-back" cx="0.9" cy="0.5" r="0.9">
        <stop offset="0" stop-color="var(--sky-light)"/>
        <stop offset="0.35" stop-color="var(--sky-mid)"/>
        <stop offset="1" stop-color="var(--sky-deep)"/>
      </radialGradient>
    </defs>
    <rect width="816" height="361" fill="url(#sky-back)"/>
    <g fill="var(--white)">
      <path d="M586 20 l3 14 l14 3 l-14 3 l-3 14 l-3 -14 l-14 -3 l14 -3z"/>
      <path d="M372 60 l2 7 l7 2 l-7 2 l-2 7 l-2 -7 l-7 -2 l7 -2z"/>
      <circle cx="300" cy="160" r="1.5"/><circle cx="460" cy="130" r="1.2"/>
      <circle cx="700" cy="50" r="1.5"/><circle cx="520" cy="200" r="1.2"/>
    </g>
    <rect role="img" aria-label="Illustration: snowy cottage with frosted trees" x="629" y="111" width="154" height="100" rx="40" fill="var(--snow)" opacity="0.9"/>
    <path d="M0 270 C120 278 200 298 300 286 C480 264 640 234 816 230 L816 361 L0 361Z" fill="var(--crimson)"/>
    <path d="M0 258 C120 266 200 286 300 274 C480 252 640 222 816 218" fill="none" stroke="var(--silver)" stroke-width="10"/>
    <path d="M0 268 C120 276 200 296 300 284 C480 262 640 232 816 228" fill="none" stroke="var(--gold)" stroke-width="4"/>
    <circle cx="156" cy="124" r="118" fill="none" stroke="var(--ring-red)" stroke-width="16"/>
    <circle role="img" aria-label="Map showing the streets around the church" cx="156" cy="124" r="108" fill="var(--map-paper)"/>
    <rect role="img" aria-label="Illustration: holly leaves and golden bells" x="40" y="210" width="100" height="80" rx="36" fill="var(--holly)"/>
  </svg>
  <ul class="service-details">
    <li>Phone: 555-317-4096</li>
    <li>Service Times: 3:00pm and 5:00pm</li>
    <li>24th DECEMBER 2011</li>
    <li>www.brookfieldfellowshipnt.com</li>
    <li>28315 Marigold Ave, Hesperia, Ca. 92345</li>
  </ul>
  <p class="church-name">Brookfield Fellowship</p>
</section>

</body>
</html>
```